Bref créative
Turnip Cuddler LLC
Embracing More Plant-Based Eating for Everyone
Bright & Fun-filled
Paula J. Mercer
Health & Wellness Coach, NQRS Certified
418 Marlow Ln.
Georgetown, KY 40871
theturnipcuddler@mailnest.example
www.turnipcuddler.example
http://twitter.com/TurnipCuddler
I do not want to have the address on the card.
Just the logo?

```html
<!DOCTYPE html>
<html lang="en">
<head>
<meta charset="UTF-8">
<title>Turnip Cuddler — Business Card</title>
<link href="https://fonts.googleapis.com/css2?family=Questrial&display=swap" rel="stylesheet">
<style>
  :root {
    --stage: #ecebe8;
    --card: #ffffff;
    --card-shade: #e9e9e9;
    --green: #4f9a2a;
    --green-deep: #2f7a1c;
    --brown: #7a5a42;
    --ink: #555555;
    --white: #ffffff;
  }
  html, body {
    margin: 0;
    padding: 0;
    width: 1200px;
    height: 972px;
    overflow: hidden;
    background: var(--stage);
    font-family: "Questrial", "Century Gothic", sans-serif;
  }
  .canvas {
    position: relative;
    width: 1200px;
    height: 972px;
  }
  .card {
    position: absolute;
    width: 570px;
    height: 330px;
    border-radius: 18px;
    overflow: hidden;
    box-shadow: 0 8px 24px rgba(0,0,0,0.18);
  }
  .card-front {
    left: 160px;
    top: 170px;
    background: var(--card);
    z-index: 2;
  }
  .card-back {
    left: 470px;
    top: 450px;
    background: linear-gradient(135deg, var(--card) 0%, var(--card-shade) 100%);
    z-index: 1;
  }
  .swoosh {
    position: absolute;
    inset: 0;
  }
  .brand-name {
    position: absolute;
    margin: 0;
    color: var(--green);
    font-weight: 400;
    white-space: nowrap;
  }
  .card-front .brand-name {
    left: 58px;
    top: 72px;
    font-size: 44px;
  }
  .identity {
    position: absolute;
    left: 20px;
    top: 148px;
    color: var(--ink);
    font-size: 12px;
    line-height: 16px;
  }
  .identity .person {
    color: var(--green-deep);
    font-size: 14px;
    margin-bottom: 2px;
  }
  .contact {
    position: absolute;
    right: 22px;
    top: 230px;
    text-align: right;
    color: var(--white);
    font-size: 11px;
    line-height: 17px;
  }
  .contact .social {
    display: inline-flex;
    align-items: center;
    gap: 5px;
  }
  .contact .social i {
    display: inline-block;
    width: 10px;
    height: 10px;
    background: var(--white);
  }
  .website {
    position: absolute;
    right: 22px;
    top: 294px;
    color: var(--white);
    font-size: 12px;
  }
  .card-back .brand-name {
    right: 40px;
    top: 250px;
    font-size: 20px;
  }
  .card-back .website {
    right: 40px;
    top: 282px;
    color: var(--ink);
    font-size: 11px;
  }
</style>
</head>
<body>
<main class="canvas">
  <section class="card card-front">
    <svg class="swoosh" width="570" height="330" viewBox="0 0 570 330">
      <path d="M0,268 C170,282 380,230 570,108 L570,330 L0,330 Z" fill="var(--green)"/>
      <path d="M0,250 C180,266 390,214 570,93" fill="none" stroke="var(--brown)" stroke-width="7"/>
      <path d="M0,236 C200,250 395,195 570,80" fill="none" stroke="var(--brown)" stroke-width="2"/>
    </svg>
    <h1 class="brand-name">Turnip Cuddler</h1>
    <div class="identity">
      <div class="person">Paula J. Mercer</div>
      <div>Health &amp; Wellness Coach</div>
      <div>NQRS Certified</div>
    </div>
    <div class="contact">
      <div>P: 859-555-0142</div>
      <div>E: theturnipcuddler@mailnest.example</div>
      <div class="social">TurnipCuddler <i></i></div>
    </div>
    <div class="website">www.turnipcuddler.example</div>
  </section>

  <section class="card card-back">
    <h2 class="brand-name">Turnip Cuddler</h2>
    <div class="website">www.turnipcuddler.example</div>
  </section>
</main>
</body>
</html>
```